Business Card Design

I need a business card designed for my business.

The company name is Rowan Pellet Group

It has four brands underneath it. They are:
- RP Events
- RP Sports Tours
- RPG Management
- Bold Mosaic

I have attached all logo items, as well as our last business card.

I look forward to seeing your designs.

Industry/Entity Type

Business

Colors
eb1f27
0355a3

Requirements
Must have
• Our contact details as per the front page of our previous business card.

```html
<!DOCTYPE html>
<html lang="en">
<head>
<meta charset="utf-8">
<title>Rowan Pellet Group – Business Card</title>
<link href="https://fonts.googleapis.com/css2?family=Quicksand:wght@400;500;700&family=Open+Sans:wght@400&display=swap" rel="stylesheet">
<style>
  :root {
    --sheet: #ffffff;
    --card-dark: #3b3b3c;
    --card-sky: #2cc1ef;
    --brand-red: #eb1f27;
    --brand-blue: #0355a3;
    --accent-blue: #2a7fd0;
    --light-text: #e8e8e8;
    --label: #222222;
  }
  * { margin: 0; padding: 0; box-sizing: border-box; }
  html, body { width: 1200px; height: 841px; overflow: hidden; background: var(--sheet); }
  .sheet { position: relative; width: 1200px; height: 841px; font-family: "Quicksand", sans-serif; }

  .card { position: absolute; overflow: hidden; }
  .card--front { left: 40px; top: 56px; width: 526px; height: 322px; background: var(--card-dark); }
  .card--back-dark { left: 606px; top: 56px; width: 516px; height: 312px; background: var(--card-dark); }
  .card--back-sky { left: 612px; top: 450px; width: 514px; height: 312px; background: var(--card-sky); }

  .caption { position: absolute; font-family: "Open Sans", sans-serif; font-size: 20px; color: var(--label); }
  .caption--front { left: 42px; top: 392px; }
  .caption--back-1 { left: 610px; top: 384px; }
  .caption--back-2 { left: 612px; top: 772px; }

  /* Front */
  .group-mark { position: absolute; left: 34px; top: 34px; }
  .group-name { position: absolute; left: 150px; top: 42px; width: 360px; font-weight: 700; font-size: 40px; line-height: 44px; color: var(--accent-blue); letter-spacing: 0.5px; }
  .group-name .group-name__sub { display: block; text-align: right; font-size: 26px; line-height: 30px; padding-right: 20px; }
  .group-rule { position: absolute; left: 150px; top: 130px; width: 200px; height: 2px; background: var(--brand-red); }

  .holder { position: absolute; left: 42px; top: 166px; }
  .holder__name { font-size: 21px; font-weight: 700; color: var(--accent-blue); line-height: 26px; }
  .holder__role { font-size: 18px; color: var(--brand-blue); line-height: 22px; }
  .contact { font-size: 16px; line-height: 22px; color: var(--light-text); }
  .contact--address { position: absolute; left: 42px; top: 234px; }
  .contact--phones { position: absolute; left: 228px; top: 172px; }
  .contact--web { position: absolute; left: 228px; top: 234px; }

  /* Backs */
  .brand-grid { position: absolute; inset: 0; display: grid; grid-template-columns: 1fr 1fr; grid-template-rows: 1fr 1fr; padding: 30px 22px; align-items: center; }
  .brand { font-weight: 700; font-size: 30px; line-height: 34px; text-align: center; }
  .brand--red { color: var(--brand-red); }
  .brand--blue { color: var(--brand-blue); }
</style>
</head>
<body>
<main class="sheet">

  <section class="card card--front" aria-label="Business card front">
    <svg class="group-mark" width="84" height="88" viewBox="0 0 84 88" aria-hidden="true">
      <circle cx="42" cy="44" r="40" fill="var(--accent-blue)"/>
    </svg>
    <div class="group-name">ROWAN PELLET<span class="group-name__sub">GROUP</span></div>
    <div class="group-rule"></div>

    <div class="holder">
      <p class="holder__name">Miles Harrow</p>
      <p class="holder__role">Principal</p>
    </div>
    <p class="contact contact--address">PO Box 418<br>Kelvin ACT 2609<br>Australia</p>
    <p class="contact contact--phones">+61 2 5550 1482<br>+61 400 555 319</p>
    <p class="contact contact--web">miles@rowanpelletgroup.com.au<br>rowanpelletgroup.com.au</p>
  </section>
  <p class="caption caption--front">Front</p>

  <section class="card card--back-dark" aria-label="Business card back, option 1">
    <div class="brand-grid">
      <p class="brand brand--red">Bold Mosaic</p>
      <p class="brand brand--blue">RPG Management</p>
      <p class="brand brand--blue">RP Events</p>
      <p class="brand brand--red">RP Sports Tours</p>
    </div>
  </section>
  <p class="caption caption--back-1">Back Option 1</p>

  <section class="card card--back-sky" aria-label="Business card back, option 2">
    <div class="brand-grid">
      <p class="brand brand--red">Bold Mosaic</p>
      <p class="brand brand--blue">RPG Management</p>
      <p class="brand brand--blue">RP Events</p>
      <p class="brand brand--red">RP Sports Tours</p>
    </div>
  </section>
  <p class="caption caption--back-2">Back Option 2</p>

</main>
</body>
</html>
```